Brackmoor Estate 2013 Solenne Cuvee

We need a label design for a 2013 Solenne Cuvee bottle, which is a premium sparkling white wine.

About Brackmoor Estate Wine (for your information):
Grown in the cool climate GI (Geographical Indicator) of Denmark, WESTERN AUSTRALIA, in the Great Southern the Brackmoor Estate vineyard is located in gravelly loam soil amidst tall Jarrah and Marri trees.

Finished label product must:
• Comply with Australian labelling requirements (see attached shiraz example)
• Fit on the face of standard sparkling wine bottle (exact bottle to be used TBA)
• Use the Brackmoor Estate logo (attached)
• Be clean, modern, and high end design
• See suitable for commercial printing

Please use the attached reserve label as a GUIDE only for your design. Foil closure colour is not determined, designers can use creativity to come up with a stylish new label. the glass colour is green, so this may change your colour scheme choices.

Will provide finalised wording details once we have received the tasting notes from the winemakers but would like to start seeing designs and colour schemes for this

Target Market(s)

Wine drinkers 25-60

Requirements
Must have
• Logo
• Name of wine- 2013 Solenne Cuvee

```html
<!DOCTYPE html>
<html lang="en">
<head>
<meta charset="utf-8">
<title>Brackmoor Estate – 2013 Solenne Cuvee Label</title>
<link rel="stylesheet" href="https://fonts.googleapis.com/css2?family=Josefin+Sans:wght@300&display=swap">
<style>
  :root {
    --page-bg: #efeeec;
    --label-top: #c8c8c8;
    --label-mid: #9c9c9c;
    --label-low: #5e5e5e;
    --label-dark: #1c1c1c;
    --label-base: #0b0b0b;
    --ink-light: #f2f2f2;
  }
  * { margin: 0; padding: 0; box-sizing: border-box; }
  html, body {
    width: 1016px;
    height: 1200px;
    overflow: hidden;
    background: var(--page-bg);
  }
  .canvas {
    position: relative;
    width: 1016px;
    height: 1200px;
  }
  .label {
    position: absolute;
    left: 343px;
    top: 30px;
    width: 330px;
    height: 1140px;
    overflow: hidden;
    background: linear-gradient(
      to bottom,
      var(--label-top) 0%,
      var(--label-mid) 36%,
      var(--label-low) 52%,
      var(--label-dark) 62%,
      var(--label-base) 100%
    );
    box-shadow: 0 6px 22px rgba(0, 0, 0, 0.25);
    font-family: "Josefin Sans", "Helvetica Neue", Arial, sans-serif;
    font-weight: 300;
    color: var(--ink-light);
  }
  .brand {
    position: absolute;
    top: 186px;
    left: 0;
    width: 100%;
    text-align: center;
  }
  .brand-mark {
    display: block;
    width: 44px;
    height: 44px;
    margin: 0 auto;
    border-radius: 50%;
    background: var(--ink-light);
    opacity: 0.9;
  }
  .brand-name {
    margin-top: 42px;
    font-size: 30px;
    letter-spacing: 0.05em;
    line-height: 1;
  }
  .landscape {
    position: absolute;
    top: 420px;
    left: 0;
    width: 100%;
    height: 260px;
    background: linear-gradient(
      to bottom,
      rgba(60, 60, 60, 0) 0%,
      rgba(60, 60, 60, 0.55) 22%,
      rgba(120, 120, 120, 0.45) 58%,
      rgba(28, 28, 28, 0.85) 86%,
      rgba(28, 28, 28, 0) 100%
    );
  }
  .wine-details {
    position: absolute;
    top: 996px;
    left: 0;
    width: 100%;
    text-align: center;
  }
  .vintage {
    font-size: 22px;
    letter-spacing: 0.22em;
    line-height: 1;
  }
  .cuvee-name {
    margin-top: 16px;
    font-size: 27px;
    letter-spacing: 0.01em;
    line-height: 1;
    text-transform: uppercase;
  }
</style>
</head>
<body>
  <main class="canvas">
    <section class="label">
      <header class="brand">
        <span class="brand-mark" aria-hidden="true"></span>
        <p class="brand-name">Brackmoor Estate</p>
      </header>
      <div class="landscape" role="img" aria-label="Black and white photograph of tall eucalyptus trees against a pale sky, fading into darkness"></div>
      <footer class="wine-details">
        <p class="vintage">2013</p>
        <p class="cuvee-name">Solenne Cuvee</p>
      </footer>
    </section>
  </main>
</body>
</html>
```